Web Design Project

We need a website design for a new website. The site will have two parts, a sales and marketing site (nothing exists at present) and an online business application, which is under construction.
The sales and marketing site needs a top level menu, and area to log into or sign up to the online applciation. Other than that we are open to suggestions.
The onlne applciations needs a similar look/feel to the marketing site and it's design needs to incorporate the following parts:
- grids
- settings page
- pop up boxes
- error messages
Please create an account on the development site at http://vorlindesk.hostpad.net to see waht functionality needs to be incorporated in the design. Needs to be viewed in FireFox.
The logo we have chosen for the site has been uploaded, please ensure all designs fit with this. I have no problems if you wish to make alterations to the logo.
- Design for both the marketing site and online application.

```html
<!DOCTYPE html>
<html lang="en">
<head>
<meta charset="utf-8">
<title>Vorlindesk</title>
<link rel="stylesheet" href="https://fonts.googleapis.com/css2?family=Open+Sans:wght@400;600;700&family=PT+Sans:wght@400;700&display=swap">
<style>
:root{
  --blue-top:#1b72b9;
  --blue-deep:#0c5597;
  --hero-a:#2a82d0;
  --hero-b:#1358a6;
  --navy:#0d3a72;
  --link:#1a6fc0;
  --green-a:#9ad01e;
  --green-b:#5f9e05;
  --green-text:#6b9a00;
  --phone-green:#5a8a00;
  --text:#555;
  --dark:#222;
  --band:#e1e1e1;
  --panel:#f0f0f0;
  --white:#fff;
}
*{box-sizing:border-box;margin:0;padding:0}
html,body{width:1200px;height:1137px;overflow:hidden;background:var(--white)}
body{font-family:"Open Sans",Arial,sans-serif;color:var(--text)}
.page{position:relative;width:1200px;height:1137px;overflow:hidden;background:var(--white)}
.abs{position:absolute}

.topbar{left:0;top:0;width:1200px;height:45px;background:linear-gradient(var(--blue-top),var(--blue-deep))}
.signin-label{left:516px;top:10px;color:var(--white);font-size:16px;white-space:nowrap}
.field{top:12px;height:20px;background:var(--white);border:1px solid #9bbbd8;font-size:13px;color:#aaa;padding:1px 7px;font-family:Arial,sans-serif}
.field.user{left:750px;width:197px}
.field.pass{left:959px;width:197px;letter-spacing:1px}
.go{left:1156px;top:12px;width:30px;height:20px;background:linear-gradient(var(--green-a),var(--green-b));border-radius:0 4px 4px 0;font-size:12px;color:#1d3a00;text-align:center;line-height:20px;font-family:Arial,sans-serif}
.account-links{right:20px;top:48px;font-size:14px;color:var(--link);font-family:Arial,sans-serif;white-space:nowrap}
.account-links .sep{margin:0 9px}

.logo-tab{left:73px;top:33px;width:335px;height:105px;background:var(--white);border-radius:0 0 50% 50% / 0 0 30px 30px;box-shadow:0 3px 6px rgba(0,0,0,.25);display:flex;align-items:center;justify-content:center;gap:12px;padding-bottom:12px}
.logo-mark{width:26px;height:26px;background:var(--link);border-radius:3px}
.logo-name{font-weight:600;font-size:40px;color:var(--green-text);letter-spacing:-1px}

.nav{left:590px;top:150px;width:597px;height:45px;border:2px solid #d6d6d6;border-radius:23px;background:var(--white);box-shadow:0 1px 3px rgba(0,0,0,.15);display:flex;align-items:center;justify-content:center;font-size:12px;font-weight:600;color:#3a3a3a;white-space:nowrap}
.nav span{white-space:nowrap}
.nav span.sep{margin:0 10px;color:#666;font-weight:400}

.header-rule{left:0;top:207px;width:1200px;height:6px;background:#e4e4e4}
.hero{left:0;top:213px;width:1200px;height:312px;background:linear-gradient(100deg,var(--hero-a),var(--hero-b))}
.hero-photo{left:12px;top:147px;width:562px;height:378px;background:linear-gradient(160deg,#d6dbe2 0%,#8e99a8 40%,#2c3440 75%,#e9ecef 100%);border-radius:60px 60px 0 0}
.hero-title{left:771px;top:264px;font-family:"PT Sans",sans-serif;font-weight:400;font-size:32px;color:var(--navy);white-space:nowrap}
.hero-text{left:771px;top:312px;width:410px;font-size:17px;line-height:21px;color:var(--white)}
.btn-green{background:linear-gradient(var(--green-a),var(--green-b));color:var(--white);border-radius:20px;box-shadow:0 1px 2px rgba(0,0,0,.3);white-space:nowrap}
.learn{left:771px;top:396px;width:158px;height:38px;font-family:"PT Sans",sans-serif;font-size:20px;display:flex;align-items:center;justify-content:center;gap:10px}

.welcome{left:0;top:525px;width:1200px;height:277px;background:var(--panel)}
.section-title{font-family:"PT Sans",sans-serif;font-weight:400;color:var(--dark);white-space:nowrap}
.section-title small{font-size:0.76em;color:#8a8a8a}
.welcome-title{left:14px;top:544px;font-size:29px}
.dotted{border-top:1px dotted #777}
.welcome-rule{left:14px;top:584px;width:806px}
.welcome-text{left:13px;top:595px;width:810px;font-size:13px;line-height:21px}
.welcome-text p+p{margin-top:21px}

.card{background:var(--white);border-radius:24px;border:1px solid #d2d2d2;box-shadow:0 0 4px rgba(0,0,0,.12)}
.app-card{left:873px;top:568px;width:313px;height:186px}
.app-title{left:888px;top:581px;font-family:"PT Sans",sans-serif;font-weight:400;font-size:27px;line-height:27px;color:var(--link)}
.app-text{left:887px;top:645px;width:185px;font-size:13px;line-height:19px}
.app-visual{left:1080px;top:610px;width:92px;height:94px;background:linear-gradient(135deg,#b9d5f0,#3f79b6 60%,#555 100%);border-radius:10px}
.demo{left:886px;top:706px;width:158px;height:36px;font-size:16px;display:flex;align-items:center;justify-content:center}

.band{left:0;top:802px;width:1200px;height:245px;background:var(--band)}
.info-card{top:827px;height:193px}
.card-a{left:12px;width:405px}
.card-b{left:430px;width:404px}
.card-c{left:847px;width:341px}
.card-title{top:842px;font-size:29px}
.body-text{font-size:13px;line-height:21px}
.dashed{border-top:1px dashed #888}
.meta{font-size:13px;color:var(--dark);white-space:nowrap}
.meta em{font-style:normal;color:var(--link)}
.more{font-size:14px;font-weight:600;color:var(--green-text);white-space:nowrap}
.subhead{font-size:16px;font-weight:600;color:var(--dark);white-space:nowrap}
.phone-num{left:927px;top:910px;font-family:Arial,sans-serif;font-size:29px;color:var(--phone-green)}
.email{left:930px;top:966px;font-family:Arial,sans-serif;font-size:19px;color:var(--link)}

.footer-links{left:27px;top:1069px;font-family:Arial,sans-serif;font-size:14px;color:var(--dark);line-height:20px}
.footer-links .sep{margin:0 9px}
.follow{left:916px;top:1075px;font-family:Arial,sans-serif;font-size:16px;color:#333}
.social{top:1064px;width:40px;height:40px;border-radius:50%;background:radial-gradient(circle at 50% 35%,#fff,#dfe4ea);border:1px solid #bfc6ce;box-shadow:0 1px 3px rgba(0,0,0,.2)}
</style>
</head>
<body>
<div class="page">

  <header>
    <div class="abs topbar"></div>
    <div class="abs signin-label">Sign In for Online Application</div>
    <div class="abs field user">User Id</div>
    <div class="abs field pass">***************</div>
    <div class="abs go">GO</div>
    <div class="abs account-links">Forgotten username or password?<span class="sep">|</span>New to Vorlindesk? Register</div>

    <div class="abs logo-tab">
      <span class="logo-mark"></span>
      <span class="logo-name">vorlindesk</span>
    </div>

    <nav class="abs nav">
      <span>HOME</span><span class="sep">|</span>
      <span>ABOUT US</span><span class="sep">|</span>
      <span>SERVICES</span><span class="sep">|</span>
      <span>SOLUTIONS</span><span class="sep">|</span>
      <span>MEMBERS</span><span class="sep">|</span>
      <span>FAQS</span><span class="sep">|</span>
      <span>CONTACT US</span>
    </nav>
    <div class="abs header-rule"></div>
  </header>

  <section>
    <div class="abs hero"></div>
    <div class="abs hero-photo" role="img" aria-label="Photo of a business team gathered around a desktop computer"></div>
    <h1 class="abs hero-title">Lorem ipsum dolor sit amet</h1>
    <p class="abs hero-text">Lorem ipsum dolor sit amet, consectetur adi piscing elit. Sed mattis gravida felis, sed luctus urna gravida quis.</p>
    <div class="abs btn-green learn">LearnMore
      <svg width="12" height="16" viewBox="0 0 12 16"><path d="M3 2l6 6-6 6" fill="none" stroke="#fff" stroke-width="2.4"/></svg>
    </div>
  </section>

  <section>
    <div class="abs welcome"></div>
    <h2 class="abs section-title welcome-title"><small>welcome to </small>Vorlindesk</h2>
    <div class="abs dotted welcome-rule"></div>
    <div class="abs welcome-text">
      <p>Lorem ipsum dolor sit amet, consectetur adipiscing elit. Sed mattis gravida felis, sed luctus urna gravida quis. Cras cursus, neque ut tempus commodo, neque leo porttitor elit, ut lacinia risus turpis non orci. Fusce lacus lacus, tristique et sagittis eget, aliquet aliquam mauris. Ut facilisis, nisl eget commodo commodo, justo purus congue dolor, ac pharetra tellus leo vitae nulla. Praesent a quam varius nulla auctor faucibus.</p>
      <p>Fusce enim tellus, pulvinar non ultrices quis, elementum ac magna. Suspendisse rutrum, nibh non lobortis pretium, dui dolor pellentesque dolor, eu molestie augue nisi a purus. Cras quis arcu in nunc pharetra fermentum quis non tellus.</p>
    </div>

    <div class="abs card app-card"></div>
    <h3 class="abs app-title">ONLINE<br>APPLICATION</h3>
    <p class="abs app-text">Lorem ipsum dolor sit amet, consectetur adipiscing elit.</p>
    <div class="abs app-visual" role="img" aria-label="Illustration of a blueprint sheet with a gear"></div>
    <div class="abs btn-green demo">Take a Demo Tour</div>
  </section>

  <section>
    <div class="abs band"></div>

    <div class="abs card info-card card-a"></div>
    <h3 class="abs section-title card-title" style="left:34px"><small>what our </small>Client Says?</h3>
    <p class="abs body-text" style="left:34px;top:882px;width:370px">Lorem ipsum dolor sit amet, consectetur adipiscing elit. Sed mattis gravida felis, sed luctus urna gravida quis. Cras cursus, ac pharetra tellus.</p>
    <div class="abs dashed" style="left:34px;top:960px;width:352px"></div>
    <div class="abs meta" style="left:38px;top:967px">Dana Hollis, CEO <em>Brightform Studio</em></div>
    <div class="abs more" style="left:316px;top:969px">View More</div>

    <div class="abs card info-card card-b"></div>
    <h3 class="abs section-title card-title" style="left:451px"><small>latest </small>News</h3>
    <div class="abs subhead" style="left:451px;top:881px">lorem ipsum dolor sit amet</div>
    <p class="abs body-text" style="left:451px;top:904px;width:370px">Lorem ipsum dolor sit amet, consectetur adipiscing elit. Sed mattis gravida felis, sed luctus urna gravida quis.</p>
    <div class="abs dashed" style="left:451px;top:960px;width:352px"></div>
    <div class="abs meta" style="left:455px;top:965px">01st January, <em>2012</em></div>
    <div class="abs more" style="left:733px;top:969px">View More</div>

    <div class="abs card info-card card-c"></div>
    <h3 class="abs section-title card-title" style="left:868px"><small>contact </small>Us</h3>
    <div class="abs subhead" style="left:868px;top:881px">Click here to get in touch with us</div>
    <svg class="abs" style="left:867px;top:910px" width="36" height="44" viewBox="0 0 36 44" aria-label="Phone">
      <rect x="6" y="2" width="22" height="38" rx="4" transform="rotate(-12 17 21)" fill="#2a2a2a"/>
      <rect x="9" y="7" width="16" height="25" rx="1" transform="rotate(-12 17 21)" fill="#3f8fd8"/>
    </svg>
    <div class="abs phone-num">888.5310.7742</div>
    <svg class="abs" style="left:867px;top:961px" width="40" height="36" viewBox="0 0 40 36" aria-label="Email">
      <rect x="3" y="6" width="32" height="22" rx="2" fill="#3aa36b"/>
      <path d="M3 7l16 12 16-12" fill="none" stroke="#bfe6cf" stroke-width="2"/>
      <circle cx="8" cy="30" r="4" fill="#f0b400"/>
    </svg>
    <div class="abs email">info@vorlindesk.co.au</div>
  </section>

  <footer>
    <div class="abs footer-links">Privacy Policy<span class="sep">|</span>Terms &amp; Conditions<br>© 2012, All Rights Reserved</div>
    <div class="abs follow">Follow Us:</div>
    <div class="abs social" style="left:1023px" aria-label="Social network"></div>
    <div class="abs social" style="left:1073px" aria-label="Social network"></div>
    <div class="abs social" style="left:1123px" aria-label="Social network"></div>
  </footer>

</div>
</body>
</html>
```